Dental Bright Keystone Brochure

We need an updated brochure/flyer for our in house dental health membership. We also want to start marketing this to businesses and will need one specifically targeted to businesses as well. Our company colors we need to start branding are red, black and white, however, we don't want the brochure to be too busy with color. We are open to ideas and want something different and eye catching.

Industry/Entity Type

Dental

Font styles to use
Serif

Colors
ec1f27
ffffff
000000

Requirements
Must have
• Brand colors; red, black and white, must have our company logo,
Should not have
• vague and random stock photos

```html
<!DOCTYPE html>
<html lang="en">
<head>
<meta charset="utf-8">
<title>Dental Bright Keystone Premier – Brochure</title>
<link rel="stylesheet" href="https://fonts.googleapis.com/css2?family=Lato:wght@400;700;900&family=Open+Sans:wght@400;600;700&display=swap">
<style>
  :root{
    --red:#c4151c;
    --red-deep:#8a0c11;
    --brand-red:#ec1f27;
    --black:#000000;
    --ink:#222222;
    --white:#ffffff;
    --grey:#cfcfcf;
    --page:#ececec;
  }
  *{box-sizing:border-box;margin:0;padding:0}
  html,body{width:900px;height:1200px;overflow:hidden}
  body{background:var(--page);font-family:"Open Sans",Arial,sans-serif;color:var(--ink);position:relative}
  .sheet{position:absolute;left:85px;width:730px;height:520px;box-shadow:0 4px 14px rgba(0,0,0,.25);overflow:hidden}
  .sheet--outer{top:60px}
  .sheet--inner{top:630px}
  .sheet-art{position:absolute;inset:0;width:730px;height:520px}
  .block{position:absolute}
  .brand{position:absolute;display:flex;flex-direction:column;align-items:center;line-height:1;font-family:"Lato",sans-serif;color:var(--ink)}
  .brand-name{font-weight:900;font-size:14px;letter-spacing:.5px;text-transform:uppercase;line-height:1}
  .brand-sub{font-weight:700;font-size:6.5px;letter-spacing:1.5px;text-transform:uppercase;line-height:1;margin-top:2px}
  .brand-line{font-family:"Open Sans",sans-serif;font-size:5px;color:#555;margin-top:2px;line-height:1}
  .tagline{font-family:"Lato",sans-serif;font-weight:900;font-size:17px;line-height:1.1;text-transform:uppercase;color:#333;white-space:nowrap}
  .tagline .accent{color:var(--red)}
  .panel-title{font-family:"Lato",sans-serif;font-weight:700;color:var(--red);font-size:14px}
  .body-copy p{font-size:8.6px;line-height:1.28;margin-bottom:9px;text-align:justify;color:#333}
  .pill{position:absolute;height:22px;border-radius:0 11px 11px 0;font-family:"Lato",sans-serif;font-weight:700;font-size:11px;display:flex;align-items:center;padding-left:10px}
  .pill--white{background:var(--white);color:var(--red)}
  .pill--red{background:var(--red-deep);color:var(--white);box-shadow:0 1px 2px rgba(0,0,0,.3)}
  .pill--center{justify-content:center;padding-left:0}
  .savings-table{width:100%;border-collapse:collapse;color:var(--white);font-size:8.2px;font-weight:700}
  .savings-table th{font-family:"Lato",sans-serif;font-size:10px;text-align:left;vertical-align:bottom;padding-bottom:6px;border-bottom:2px solid var(--black);line-height:1}
  .savings-table td{padding:1.6px 0;line-height:1.15;white-space:nowrap}
  .savings-table tr:first-child td{padding-top:12px}
  .savings-table .amount{width:66px}
  .note-dark{font-size:8.2px;line-height:1.25;color:#3a0608}
  .address{font-family:"Lato",sans-serif;font-weight:700;font-size:11px;text-align:center;color:var(--ink)}
  .phone{font-family:"Lato",sans-serif;font-weight:900;font-size:19px;color:var(--red);text-align:center;display:flex;align-items:center;justify-content:center;gap:5px;line-height:1}
  .web-button{background:var(--black);color:var(--white);font-family:"Lato",sans-serif;font-weight:700;font-size:13px;border-radius:8px 8px 0 0;display:flex;align-items:center;justify-content:center}
  .cover-title{font-family:"Lato",sans-serif;font-weight:900;color:var(--white);font-size:21px;line-height:1.05;text-align:center}
  .cover-sub{font-size:8.6px;line-height:1.25;color:#3a0608;text-align:center;font-weight:600}
  .list{list-style:none;font-size:8.3px;line-height:1.22}
  .list li{position:relative;padding-left:11px;margin-bottom:1px}
  .list li::before{content:"";position:absolute;left:0;top:3px;width:4px;height:4px;background:currentColor}
  .list--light{color:var(--white);font-weight:600}
  .list--dark{color:#222;font-weight:600}
  .list--dark li::before{background:var(--red)}
  .list--spaced li{margin-bottom:6px}
  .list .nob::before{display:none}
  .lead-light{color:var(--white);font-size:8.4px;line-height:1.25}
  .copy-dark{font-size:8.3px;line-height:1.25;color:#222;font-weight:600}
  .copy-red{font-size:8.3px;line-height:1.25;color:var(--red);font-weight:600}
  .cost{color:var(--white);font-size:8.3px;line-height:1.25;font-weight:600}
  .catch-title{font-family:"Lato",sans-serif;font-weight:700;color:var(--red);font-size:11px;text-align:center}
  .catch .list{color:#222}
  .catch .list li::before{background:var(--black)}
  .footnote{font-size:7.8px;line-height:1.25;color:var(--red);font-weight:600}
</style>
</head>
<body>

<!-- Outer face -->
<section class="sheet sheet--outer">
  <svg class="sheet-art" viewBox="0 0 730 520">
    <defs>
      <linearGradient id="outerHeader" x1="0" x2="1" y1="0" y2="0">
        <stop offset="0" stop-color="#d6d6d6"/><stop offset=".5" stop-color="#ffffff"/><stop offset="1" stop-color="#f4f4f4"/>
      </linearGradient>
      <linearGradient id="greyPanel" x1="0" x2="1">
        <stop offset="0" stop-color="#a9a9a9"/><stop offset=".55" stop-color="#f2f2f2"/><stop offset="1" stop-color="#ffffff"/>
      </linearGradient>
      <linearGradient id="redPanel" x1="0" x2="1">
        <stop offset="0" stop-color="#7d0a0f"/><stop offset=".5" stop-color="#c4151c"/><stop offset="1" stop-color="#8a0c11"/>
      </linearGradient>
      <linearGradient id="photoSmiles" x1="0" x2="1" y1="0" y2="1">
        <stop offset="0" stop-color="#f1dfcf"/><stop offset=".5" stop-color="#d8b59a"/><stop offset="1" stop-color="#efe7e2"/>
      </linearGradient>
      <linearGradient id="photoFamily" x1="0" x2="1">
        <stop offset="0" stop-color="#e8d3c2"/><stop offset="1" stop-color="#f6f2ef"/>
      </linearGradient>
    </defs>
    <rect width="730" height="520" fill="#ffffff"/>
    <rect width="730" height="80" fill="url(#outerHeader)"/>
    <path d="M0 80 C 260 58, 500 62, 730 72 L730 80 L0 80Z" fill="#8a0c11"/>
    <rect x="0" y="80" width="245" height="300" fill="url(#greyPanel)"/>
    <rect x="245" y="80" width="240" height="300" fill="url(#redPanel)"/>
    <rect x="485" y="80" width="245" height="330" fill="url(#photoSmiles)" role="img" aria-label="Photo of two smiling young women"/>
    <path d="M0 366 C 220 406, 470 414, 730 372 L730 520 L0 520Z" fill="#ffffff"/>
    <rect x="0" y="388" width="245" height="132" fill="url(#photoFamily)" role="img" aria-label="Photo of a smiling family of four"/>
    <path d="M485 418 C 580 410, 660 396, 730 382 L730 520 L485 520Z" fill="url(#redPanel)"/>
    <path d="M0 362 C 220 402, 470 410, 730 366" fill="none" stroke="#000" stroke-width="6"/>
    <path d="M0 372 C 220 412, 470 420, 730 376" fill="none" stroke="#ffffff" stroke-width="3"/>
  </svg>

  <div class="brand" style="left:500px;top:30px">
    <span class="brand-name">Harlow</span>
    <span class="brand-sub">Dental Care</span>
  </div>
  <div class="block tagline" style="left:590px;top:14px">Better Smiles<br>Better Health<br><span class="accent">...A Better Life</span></div>

  <div class="block" style="left:25px;top:100px;width:205px">
    <h2 class="panel-title">Dental Bright Keystone Premier</h2>
  </div>
  <div class="block body-copy" style="left:25px;top:130px;width:200px">
    <p>includes 100% of your preventive care—cleanings, x-rays, checkup exams—with zero co-pay. It makes it affordable and easy for you to keep up your optimal schedule of preventive visits to maintain your health.</p>
    <p>Premier membership is a simple agreement between you and Harlow Dental Care; there's no third party involved, no claims to fill out and no worry about whether your claim will be approved.</p>
    <p>You will know what your benefit and bottom line cost is before you start treatment.</p>
    <p>Joining is a no-brainer: even if all you need are your regular cleanings, x-rays and exams you will save money. And if you do need more dental work, you will save more, potentially a lot more.</p>
  </div>

  <div class="pill pill--white" style="left:245px;top:84px;width:185px;height:26px;font-size:9.5px;line-height:1.05">Benefits are the amounts that<br>will be deducted from</div>
  <div class="block" style="left:258px;top:122px;width:215px">
    <table class="savings-table">
      <thead><tr><th>Service</th><th class="amount">Premier Benefit<br>your savings</th></tr></thead>
      <tbody>
        <tr><td>Whitening</td><td class="amount">$130</td></tr>
        <tr><td>Composite (white) fillings</td><td class="amount">$40 - $70</td></tr>
        <tr><td>Root canals</td><td class="amount">$100</td></tr>
        <tr><td>Crowns, any type</td><td class="amount">$150</td></tr>
        <tr><td>Bridges</td><td class="amount">$300 - $600</td></tr>
        <tr><td>Porcelain veneers</td><td class="amount">$170</td></tr>
        <tr><td>Complete denture, upper or lower</td><td class="amount">$300</td></tr>
        <tr><td>Partial denture, upper or lower</td><td class="amount">$250</td></tr>
        <tr><td>Orthodontics</td><td class="amount">$400 - $500</td></tr>
        <tr><td>Nightguards</td><td class="amount">$50</td></tr>
        <tr><td style="padding-top:6px">Implants</td><td class="amount" style="padding-top:6px">$250</td></tr>
      </tbody>
    </table>
    <p class="note-dark" style="margin-top:16px">This is a partial list; benefits apply on all services we offer. You will receive an exact quote showing your savings on any proposed treatment.</p>
  </div>

  <div class="brand" style="left:245px;top:410px;width:240px">
    <span class="brand-name">Harlow</span>
    <span class="brand-sub">Dental Care</span>
  </div>
  <div class="block address" style="left:245px;top:442px;width:240px">18 Birch Lane Westbrook, Maine 04092</div>
  <div class="block phone" style="left:245px;top:460px;width:240px">
    <svg width="14" height="14" viewBox="0 0 14 14" aria-hidden="true"><rect width="14" height="14" rx="2" fill="#c4151c"/><path d="M4 3.2c.5-.4 1-.3 1.3.2l.7 1.3c.2.4.1.8-.2 1l-.5.4c.4 1 1.1 1.8 2.1 2.3l.4-.5c.3-.3.7-.4 1-.2l1.3.7c.5.3.6.8.2 1.3-.6.8-1.5 1-2.4.6C5.8 9.5 4.5 8.2 3.6 6.1 3.2 5.1 3.4 4 4 3.2z" fill="#fff"/></svg>
    207-555-0148
  </div>
  <div class="block web-button" style="left:262px;top:487px;width:206px;height:33px">www.HarlowDentalCare.com</div>

  <div class="block cover-title" style="left:490px;top:432px;width:235px">Dental Bright<br>Keystone Premier</div>
  <div class="block cover-sub" style="left:505px;top:482px;width:205px">Our exclusive membership plan, giving you benefits on every dental service we offer!</div>
</section>

<!-- Inner face -->
<section class="sheet sheet--inner">
  <svg class="sheet-art" viewBox="0 0 730 520">
    <defs>
      <linearGradient id="redLeft" x1="0" x2="1">
        <stop offset="0" stop-color="#9c0d13"/><stop offset=".6" stop-color="#c4151c"/><stop offset="1" stop-color="#a50f15"/>
      </linearGradient>
      <linearGradient id="greyMid" x1="0" x2="1">
        <stop offset="0" stop-color="#ffffff"/><stop offset=".6" stop-color="#ebebeb"/><stop offset="1" stop-color="#b9b9b9"/>
      </linearGradient>
      <linearGradient id="faintFamily" x1="0" x2="1" y1="0" y2="1">
        <stop offset="0" stop-color="#b3131a"/><stop offset="1" stop-color="#7d0a0f"/>
      </linearGradient>
    </defs>
    <rect x="0" y="0" width="245" height="520" fill="url(#redLeft)"/>
    <rect x="0" y="370" width="245" height="150" fill="url(#faintFamily)" role="img" aria-label="Faint red-toned photo of a smiling family"/>
    <rect x="245" y="0" width="240" height="520" fill="url(#greyMid)"/>
    <rect x="485" y="0" width="245" height="520" fill="url(#redLeft)"/>
    <path d="M485 402 C 560 372, 650 362, 730 376 L730 520 L485 520Z" fill="#ffffff"/>
    <path d="M485 392 C 560 362, 650 352, 730 366" fill="none" stroke="#000" stroke-width="6"/>
    <path d="M245 465 C 320 475, 420 470, 485 455 L485 520 L245 520Z" fill="#ffffff"/>
  </svg>

  <div class="pill pill--white" style="left:15px;top:33px;width:170px">Advantages:</div>
  <div class="block" style="left:18px;top:68px;width:215px">
    <p class="lead-light"><b>It's not insurance;</b> no third party; no red tape<br><b>Affordable</b> predictable cost, automatic payments</p>
    <ul class="list list--light" style="margin-top:6px">
      <li>No waiting period</li>
      <li>No deductible ever</li>
      <li>No annual maximum</li>
      <li>No claim forms, no claims to be denied, no stalled payments</li>
      <li>No pre-authorizations</li>
      <li>Choice of coverage to fit your needs; tailor your plan to fit you • Know your exact coverage before treatment</li>
      <li>You choose the treatment; no third party interference</li>
      <li>Includes benefits for cosmetic dentistry and orthodontics, and other services</li>
    </ul>
  </div>
  <div class="pill pill--white" style="left:15px;top:258px;width:170px">What's included?</div>
  <div class="block" style="left:18px;top:290px;width:215px">
    <p class="lead-light" style="font-weight:700">Preventive services at 100%:</p>
    <ul class="list list--light" style="margin-top:4px">
      <li>Your regular twice-a-year cleanings or 4-times-a-year periodontal maintenance</li>
      <li>Dental exam by the doctor each year</li>
      <li>Necessary x-rays</li>
      <li>Fluoride treatments</li>
    </ul>
  </div>

  <div class="pill pill--red pill--center" style="left:305px;top:30px;width:160px">Plus:</div>
  <div class="block" style="left:255px;top:58px;width:220px">
    <ul class="list list--dark">
      <li>Teeth whitening — 50% off</li>
      <li>Benefits for fillings, crowns, bridges, orthodontics, veneers and implants</li>
    </ul>
  </div>
  <div class="pill pill--red" style="left:245px;top:92px;width:215px;padding-left:30px">How do I qualify?</div>
  <div class="block" style="left:268px;top:122px;width:207px">
    <p class="copy-dark">You must be a patient of record of Harlow Dental Care in good standing (you may sign up after your initial exam, if you are a new patient)</p>
    <p class="copy-red">You agree to partner with us to create the savings:</p>
    <ul class="list list--dark list--spaced" style="margin-top:5px">
      <li>Keep your appointments with us on time as scheduled</li>
      <li>Keep your account balance zero by paying at the time of service or before</li>
      <li>No insurance claims to file.</li>
      <li>If you do have insurance, you may still qualify if you file claims yourself (we will print the form for you), and make payment to us in full before treatment. The insurance payment will then go to you.</li>
    </ul>
  </div>
  <div class="pill pill--red" style="left:245px;top:300px;width:215px;padding-left:30px">How does it work?</div>
  <div class="block" style="left:268px;top:330px;width:207px">
    <ul class="list list--dark list--spaced">
      <li>Yearly membership fee divided into 12 monthly payments • Monthly payments charged to your credit or debit card automatically, or automatic withdrawals from your bank account</li>
      <li>Membership renews each year automatically</li>
      <li class="nob">Basic Plan includes: 100% coverage for two cleanings and fluoride treatments per year, x-rays, and one exam by the doctor</li>
    </ul>
  </div>
  <div class="brand" style="left:245px;top:482px;width:240px">
    <span class="brand-name" style="font-size:11px">Harlow</span>
    <span class="brand-sub" style="font-size:5.5px">Dental Care</span>
    <span class="brand-line">better smiles, better health ...a better life</span>
  </div>

  <div class="block" style="left:498px;top:18px;width:222px">
    <ul class="list list--light list--spaced">
      <li>Periodontal Maintenance Plan includes: 100% coverage for four periodontal maintenance visits per year, x-rays, fluoride treatments, doctor exam</li>
      <li>Nothing to pay when you come for your regular visit with the hygienist</li>
      <li>Both plans include benefits for all other services we offer</li>
      <li>Includes benefits for elective treatment not covered by most dental insurance plans • No yearly maximum on benefits</li>
      <li>Benefits are clearly spelled out; no guessing Membership benefits apply only to services provided directly by Harlow Dental Care in our office</li>
    </ul>
  </div>
  <div class="pill pill--white" style="left:485px;top:198px;width:185px;padding-left:25px">What's the cost?</div>
  <div class="block cost" style="left:498px;top:228px;width:222px">
    <ul class="list list--light">
      <li>Set-up Fee (applies to all plans)</li>
      <li>$45 per person, $90 maximum per family<br>Basic preventive plan:<br>two preventive visits per year, restorative benefits:</li>
      <li>Individual: $27 per month<br>Periodontal maintenance plan:<br>four maintenance visits/yr., restorative benefits:</li>
      <li>Individual: $52 per month</li>
      <li>Children* (under 18), basic preventive plan: $20 per month</li>
    </ul>
  </div>

  <div class="block catch-title" style="left:485px;top:386px;width:245px">What's the catch?</div>
  <div class="block catch" style="left:498px;top:410px;width:222px">
    <ul class="list">
      <li style="color:var(--red)">No catch, no hidden costs.</li>
      <li style="color:var(--red)">This plan reflects the fact that those who meet the conditions outlined above reduce our costs. These savings are passed back to you.</li>
    </ul>
    <p class="footnote" style="margin-top:9px;padding-left:11px">*Immediate family living in same household as parent who is a member of this plan</p>
  </div>
</section>

</body>
</html>
```